Back Pain

Need a flyer similar to the attached draft. This is to be handed out to prospective patients. Note that Sketch Hive has already designed the logo. If you need a copy please contact me

```html
<!DOCTYPE html>
<html lang="en">
<head>
<meta charset="utf-8">
<title>Tech Neck – Spine Ease Clinic Flyer</title>
<link rel="stylesheet" href="https://fonts.googleapis.com/css2?family=Oswald:wght@400;500;600;700&family=Open+Sans:wght@400;600;700&display=swap">
<style>
  :root {
    --panel-blue: #1f6aa6;
    --ink-blue: #1d5d99;
    --green: #8cc63f;
    --deep-green: #2d5a1c;
    --label-teal: #3f97b4;
    --label-teal-fade: rgba(63,151,180,0);
    --offer-yellow: #ece94d;
    --offer-red: #8c1b1b;
    --white: #ffffff;
  }
  html, body {
    margin: 0;
    padding: 0;
    width: 1200px;
    height: 1200px;
    overflow: hidden;
    background: var(--white);
  }
  .flyer {
    position: absolute;
    left: 141px;
    top: 6px;
    width: 918px;
    height: 1188px;
    background: var(--white);
    font-family: "Oswald", sans-serif;
    overflow: hidden;
  }
  .side-panel {
    position: absolute;
    left: 0; top: 0;
    width: 390px;
    height: 1045px;
    background: var(--panel-blue);
  }
  .title {
    position: absolute;
    left: 34px; top: 16px;
    margin: 0;
    font-size: 80px;
    font-weight: 500;
    color: var(--green);
    letter-spacing: 1px;
    line-height: 1;
  }
  .person-photo {
    position: absolute;
    left: 55px; top: 165px;
    width: 270px;
    height: 625px;
    border-radius: 120px 120px 20px 20px;
    background: linear-gradient(180deg, #2b2b2b 0%, #e8e6e2 30%, #8a7a50 55%, #c43a55 95%);
    opacity: 0.85;
  }
  .symptom {
    position: absolute;
    height: 30px;
    line-height: 30px;
    padding-right: 10px;
    text-align: right;
    color: var(--white);
    font-size: 20px;
    font-weight: 500;
    white-space: nowrap;
    background: linear-gradient(90deg, var(--label-teal-fade) 0%, var(--label-teal) 45%, var(--label-teal) 100%);
  }
  .divider-dotted {
    position: absolute;
    left: 30px; top: 914px;
    width: 338px;
    border-top: 2px dotted rgba(255,255,255,0.6);
  }
  .practitioner {
    position: absolute;
    left: 0; top: 940px;
    width: 390px;
    text-align: center;
    color: var(--white);
    font-family: "Open Sans", sans-serif;
    font-size: 20px;
    line-height: 25px;
  }
  .practitioner strong { font-size: 23px; font-weight: 700; display: block; margin-bottom: 2px; }

  .brand {
    position: absolute;
    left: 560px; top: 100px;
    width: 340px;
    text-align: center;
    color: var(--ink-blue);
  }
  .brand-name {
    display: inline-flex;
    align-items: center;
    gap: 8px;
    font-size: 24px;
    font-weight: 600;
    letter-spacing: 0.5px;
  }
  .brand-dot {
    width: 16px; height: 16px;
    border-radius: 50%;
    background: var(--green);
  }
  .brand-sub {
    font-size: 13px;
    font-weight: 500;
    letter-spacing: 1px;
    color: var(--ink-blue);
    margin-top: 2px;
  }

  .chart-heading {
    position: absolute;
    left: 536px; top: 208px;
    margin: 0;
    font-size: 21px;
    font-weight: 600;
    line-height: 23px;
    color: var(--ink-blue);
  }
  .tilt-chart {
    position: absolute;
    left: 520px; top: 250px;
  }
  .tilt-chart text { font-family: "Oswald", sans-serif; }

  .device-stat {
    position: absolute;
    left: 440px; top: 512px;
  }
  .stat-text {
    position: absolute;
    left: 554px; top: 512px;
    color: var(--ink-blue);
    font-size: 21px;
    font-weight: 600;
    line-height: 1.3;
  }
  .stat-text .stat-figure {
    display: block;
    color: var(--green);
    font-size: 33px;
    line-height: 1.15;
  }

  .message {
    position: absolute;
    left: 420px; top: 650px;
    width: 478px;
    text-align: center;
    color: var(--ink-blue);
    font-weight: 600;
    white-space: nowrap;
  }
  .message .accent { color: var(--green); }
  .msg-line-1 { font-size: 34px; line-height: 46px; letter-spacing: 0.5px; }
  .msg-banner {
    margin: 12px 10px 0;
    height: 46px;
    line-height: 46px;
    background: var(--green);
    color: var(--deep-green);
    font-size: 22px;
    font-weight: 500;
    letter-spacing: 0.5px;
  }
  .msg-line-3 { font-size: 34px; line-height: 42px; margin-top: 6px; letter-spacing: 0.5px; }
  .msg-line-4 { font-size: 55px; line-height: 62px; font-weight: 500; letter-spacing: 0.5px; }
  .msg-of-the {
    display: flex;
    align-items: center;
    gap: 14px;
    margin: 2px 10px 0;
    color: var(--green);
    font-size: 24px;
    line-height: 30px;
  }
  .msg-of-the::before, .msg-of-the::after {
    content: "";
    flex: 1;
    border-top: 3px solid var(--ink-blue);
  }
  .msg-neck {
    font-size: 126px;
    font-weight: 700;
    line-height: 124px;
    letter-spacing: 10px;
    text-align: left;
    padding-left: 60px;
    text-shadow: 5px 4px 0 var(--green);
  }

  .offer {
    position: absolute;
    left: 0; top: 1045px;
    width: 918px;
    height: 143px;
    background: var(--offer-yellow);
    text-align: center;
  }
  .offer-headline {
    margin: 28px 0 0;
    color: var(--offer-red);
    font-family: "Open Sans", sans-serif;
    font-size: 33px;
    font-weight: 700;
    line-height: 40px;
  }
  .offer-detail {
    color: var(--ink-blue);
    font-family: "Open Sans", sans-serif;
    font-size: 15px;
    line-height: 22px;
  }
</style>
</head>
<body>
<main class="flyer">
  <section class="side-panel">
    <h1 class="title">TECH NECK</h1>
    <div class="person-photo" role="img" aria-label="Photo of a young man with a backpack looking down at his phone"></div>
    <div class="divider-dotted"></div>
    <div class="practitioner">
      <strong>Dr. Samuel Whitford</strong>
      Now in Portside at:<br>
      42 Harbour Rd., Quay Suites
    </div>
  </section>

  <div class="symptom" style="left:296px; top:210px; width:132px;">HEADACHES</div>
  <div class="symptom" style="left:266px; top:253px; width:102px;">NECK PAIN</div>
  <div class="symptom" style="left:326px; top:298px; width:147px;">SHOULDER PAIN</div>
  <div class="symptom" style="left:273px; top:348px; width:167px;">ARM &amp; HAND PAIN</div>
  <div class="symptom" style="left:258px; top:393px; width:107px;">BACK PAIN</div>
  <div class="symptom" style="left:236px; top:463px; width:102px;">SCIATICA</div>

  <div class="brand">
    <div class="brand-name"><span class="brand-dot"></span>SPINE EASE CLINIC</div>
    <div class="brand-sub">DR SAM WHITFORD • CHIROPRACTOR</div>
  </div>

  <h2 class="chart-heading">AS THE HEAD TILTS FORWARD<br>MORE FORCE IS PLACED<br>ON THE SPINE</h2>

  <svg class="tilt-chart" width="300" height="230" viewBox="0 0 300 230" aria-label="Pressure on spine by degrees of forward head tilt">
    <rect x="16" y="50" width="40" height="30" rx="4" fill="var(--ink-blue)" role="img" aria-label="Forward head tilt icon"/>
    <g fill="var(--green)">
      <rect x="14" y="119" width="34" height="51"/>
      <rect x="62" y="78" width="34" height="92"/>
      <rect x="110" y="62" width="34" height="108"/>
      <rect x="158" y="35" width="34" height="135"/>
      <rect x="208" y="8" width="34" height="162"/>
    </g>
    <g fill="var(--white)" font-size="17" font-weight="500" text-anchor="middle">
      <text x="31" y="150">12</text>
      <text x="79" y="102">27</text>
      <text x="127" y="86">40</text>
      <text x="175" y="59">49</text>
      <text x="225" y="32">60</text>
    </g>
    <g fill="var(--ink-blue)" font-size="20" font-weight="600" text-anchor="middle">
      <text x="31" y="196">0°</text>
      <text x="79" y="196">15°</text>
      <text x="127" y="196">30°</text>
      <text x="175" y="196">45°</text>
      <text x="225" y="196">60°</text>
    </g>
    <text x="16" y="220" fill="var(--ink-blue)" font-size="15" font-weight="500">DEGREES OF FORWARD HEAD TILT</text>
    <text transform="translate(275,170) rotate(-90)" fill="var(--ink-blue)" font-size="14" font-weight="500">PRESSURE ON SPINE (LBS)</text>
  </svg>

  <svg class="device-stat" width="100" height="100" viewBox="0 0 100 100" aria-label="Pie chart of daily device use">
    <circle cx="50" cy="50" r="48" fill="var(--green)"/>
    <path d="M50 50 L50 2 A48 48 0 0 1 74 91.6 Z" fill="var(--ink-blue)"/>
  </svg>
  <div class="stat-text">
    THE AVERAGE PERSON SPENDS
    <span class="stat-figure">8-11 HOURS PER DAY</span>
    USING ELECTRONIC DEVICES
  </div>

  <section class="message">
    <div class="msg-line-1">CHIROPRACTIC CARE <span class="accent">CAN HELP</span></div>
    <div class="msg-banner">CORRECT AND PREVENT THESE PROBLEMS</div>
    <div class="msg-line-3">BY RESTORING <span class="accent">AND</span> MAINTAINING</div>
    <div class="msg-line-4">PROPER ALIGNMENT</div>
    <div class="msg-of-the">OF THE</div>
    <div class="msg-neck">NECK</div>
  </section>

  <footer class="offer">
    <p class="offer-headline">50% OFF INITIAL CONSULTATION</p>
    <div class="offer-detail">if you book online at www.spineeaseclinic.com.au<br>choose tech neck option</div>
  </footer>
</main>
</body>
</html>
```